Riverstone & Pine Construction and Developments business cards

A business card with watermark background (construction work)

Company logo attached

Home improvement projects
House renovations
Bathroom and kitchen renovations
House extensions
New builds and granny flats

Director Omar Haddine
(Phone number)
omar@rpcbuildgroup.com.au
(Instagram logo) rpc_buildgroup

```html
<!DOCTYPE html>
<html lang="en">
<head>
<meta charset="utf-8">
<title>Riverstone &amp; Pine Construction and Developments – Business Cards</title>
<link rel="stylesheet" href="https://fonts.googleapis.com/css2?family=Montserrat:wght@700&family=Roboto:wght@400;500;700&display=swap">
<style>
  :root {
    --backdrop: #2a2b2e;
    --brand-blue: #1e72c2;
    --brand-blue-deep: #1865b0;
    --band-grey: #3e4248;
    --paper: #f3f4f6;
    --ink: #2c2f33;
    --white: #ffffff;
  }
  * { box-sizing: border-box; margin: 0; padding: 0; }
  html, body {
    width: 1200px; height: 1050px; overflow: hidden;
    background: var(--backdrop);
    font-family: "Roboto", Arial, sans-serif;
  }
  .stage {
    position: relative; width: 1200px; height: 1050px;
  }
  .card {
    position: absolute; left: 320px; width: 560px; height: 340px;
    border-radius: 24px; overflow: hidden;
    box-shadow: 0 14px 30px rgba(0,0,0,0.45);
  }

  /* Front card */
  .card--front { top: 150px; background: var(--brand-blue); }
  .brand-lockup {
    position: absolute; display: flex; align-items: center; gap: 14px;
  }
  .brand-mark {
    width: 18px; height: 18px; background: var(--white); flex: none;
  }
  .brand-name {
    font-family: "Montserrat", Arial, sans-serif; font-weight: 700;
    color: var(--white); line-height: 1.15;
  }
  .card--front .brand-lockup { left: 0; right: 0; top: 48px; justify-content: center; }
  .card--front .brand-name { font-size: 25px; text-align: left; }

  .services-band {
    position: absolute; left: 0; right: 0; top: 212px; height: 66px;
    background: var(--band-grey);
    display: flex; flex-direction: column; justify-content: center; align-items: center;
    gap: 5px; color: var(--white); font-size: 14.5px;
  }
  .services-band .sep { padding: 0 7px; }
  .social-row {
    position: absolute; left: 0; right: 0; bottom: 20px;
    display: flex; justify-content: center; gap: 34px;
    color: var(--white); font-size: 14.5px;
  }
  .social-row span { display: flex; align-items: center; gap: 8px; }

  /* Back card */
  .card--back { top: 560px; background: var(--paper); }
  .back-panel { position: absolute; inset: 0; }
  .card--back .brand-lockup { left: 26px; top: 128px; width: 200px; gap: 10px; }
  .card--back .brand-mark { width: 15px; height: 15px; }
  .card--back .brand-name { font-size: 16px; }

  .contact {
    position: absolute; left: 322px; top: 62px; color: var(--ink);
  }
  .contact-name {
    font-size: 23px; font-weight: 700; color: var(--brand-blue); letter-spacing: 0.2px;
  }
  .contact-role { font-size: 14px; margin-top: 3px; }
  .contact-list { list-style: none; margin-top: 22px; }
  .contact-list li {
    display: flex; align-items: center; gap: 10px; font-size: 14px; height: 24px;
  }
  .icon { width: 15px; height: 15px; flex: none; }
</style>
</head>
<body>
<main class="stage">

  <section class="card card--front" aria-label="Business card front">
    <div class="brand-lockup">
      <span class="brand-mark"></span>
      <p class="brand-name">Riverstone &amp; Pine<br>Construction<br>and Developments</p>
    </div>
    <div class="services-band">
      <p>Home Improvement Projects<span class="sep">|</span>House Renovations<span class="sep">|</span>House Extensions</p>
      <p>Bathroom &amp; Kitchen Renovations<span class="sep">|</span>New Builds &amp; Granny Flats</p>
    </div>
    <div class="social-row">
      <span>
        <svg class="icon" viewBox="0 0 16 16"><circle cx="8" cy="8" r="6.5" fill="none" stroke="#fff" stroke-width="1.5"/></svg>
        rpc_buildgroup
      </span>
      <span>
        <svg class="icon" viewBox="0 0 16 16" fill="none" stroke="#fff" stroke-width="1.3"><circle cx="8" cy="8" r="6.5"/><ellipse cx="8" cy="8" rx="3" ry="6.5"/><path d="M1.5 8h13"/></svg>
        rpcbuildgroup.com.au
      </span>
    </div>
  </section>

  <section class="card card--back" aria-label="Business card back">
    <svg class="back-panel" viewBox="0 0 560 340" preserveAspectRatio="none">
      <path d="M0 0 H268 C248 110 262 240 318 340 H0 Z" fill="var(--band-grey)"/>
      <path d="M0 0 H248 C228 110 242 240 296 340 H0 Z" fill="var(--brand-blue)"/>
    </svg>
    <div class="brand-lockup">
      <span class="brand-mark"></span>
      <p class="brand-name">Riverstone &amp; Pine<br>Construction<br>and Developments</p>
    </div>
    <div class="contact">
      <h1 class="contact-name">Omar Haddine</h1>
      <p class="contact-role">Managing Director</p>
      <ul class="contact-list">
        <li>
          <svg class="icon" viewBox="0 0 16 16"><circle cx="8" cy="8" r="7" fill="var(--brand-blue)"/><path d="M5.2 4.3l1.3-.4 1 2-.8.7c.4.9 1 1.5 1.9 1.9l.7-.8 2 1-.4 1.3c-2.9.2-5.9-2.8-5.7-5.7z" fill="#fff"/></svg>
          0400 318 274
        </li>
        <li>
          <svg class="icon" viewBox="0 0 16 16" fill="none" stroke="var(--brand-blue)" stroke-width="1.4"><rect x="1.5" y="3.5" width="13" height="9" rx="1"/><path d="M1.5 4l6.5 5 6.5-5"/></svg>
          omar@rpcbuildgroup.com.au
        </li>
        <li>
          <svg class="icon" viewBox="0 0 16 16" fill="none" stroke="var(--brand-blue)" stroke-width="1.3"><circle cx="8" cy="8" r="6.5"/><ellipse cx="8" cy="8" rx="3" ry="6.5"/><path d="M1.5 8h13"/></svg>
          rpcbuildgroup.com.au
        </li>
        <li>
          <svg class="icon" viewBox="0 0 16 16"><circle cx="8" cy="8" r="6.5" fill="none" stroke="var(--brand-blue)" stroke-width="1.5"/></svg>
          rpc_buildgroup
        </li>
      </ul>
    </div>
  </section>

</main>
</body>
</html>
```